Mexican Restaurant needs a new Menu Design

Mexican restaurant LA TORTUGA VERDE is renewing its menu, so we need something new.
Since our inception we have given the task of rescuing ingredients, recipes, and traditional and representatives dishes of the culinary techniques of yesteryear.
We are the only restaurant in Guadalajara that manufactures its own dairy natural as fresh cheese, the cream and our already well-known and traditional jocoqui. In addition, we produce organic ranch egg and are currently in the development of organic vegetables cultivated on the slopes of the old Hill which gives our plants benefit from an exceptional microclimate.
Find more information about the restaurant in www.latortugaverde.com.
The menu needs to have the full list of products with the prices, some phrases that speak of the philosophy of the ranch-style-living, photos.
We need the cover, back cover and interiors.
Updates
Thank you so much for the proposals you have submitted for the menu design. We are looking them carefully.
Thank you very much for taking your time to design a proposal for our menu!!!
Target Market(s)
The target is very wide (28-40 yrs.): Young executives, Young families, Housewives.
Industry/Entity Type
Restaurant
Look and feel
Each slider illustrates characteristics of the customer's brand and the style your logo design should communicate.

```html
<!DOCTYPE html>
<html lang="es">
<head>
<meta charset="utf-8">
<title>La Tortuga Verde – Menú, páginas 3 y 4</title>
<link href="https://fonts.googleapis.com/css2?family=Marcellus&family=Mako&family=Alegreya:wght@700&display=swap" rel="stylesheet">
<style>
  :root {
    --canvas: #efefef;
    --frame-red: #e31e24;
    --brush-red: #dc1f22;
    --parchment-light: #f6ead0;
    --parchment-mid: #efdcb4;
    --parchment-dark: #e6cd9c;
    --ink: #2b2622;
    --ink-soft: #3c352f;
    --rule: #4a423a;
    --page-num: #5a524a;
    --chili-dark: #3a0f0c;
    --chili-mid: #6d1c14;
  }
  * { box-sizing: border-box; margin: 0; padding: 0; }
  html, body { width: 1200px; height: 901px; overflow: hidden; background: var(--canvas); }
  .canvas { position: relative; width: 1200px; height: 901px; }

  .menu-page {
    position: absolute; top: 30px; height: 727px;
    border: 4px solid var(--frame-red);
    background:
      radial-gradient(ellipse at 70% 20%, var(--parchment-light) 0%, transparent 60%),
      radial-gradient(ellipse at 20% 80%, var(--parchment-light) 0%, transparent 55%),
      linear-gradient(160deg, var(--parchment-mid), var(--parchment-dark) 50%, var(--parchment-mid));
  }
  .menu-page--left { left: 22px; width: 570px; }
  .menu-page--right { left: 609px; width: 570px; }

  .page-number {
    position: absolute; top: 6px; right: 14px;
    font: 17px "Marcellus", serif; color: var(--page-num);
  }

  .dish { position: absolute; width: 532px; }
  .menu-page--left .dish { left: 14px; }
  .menu-page--right .dish { left: 13px; }
  .dish__head {
    display: flex; justify-content: space-between; align-items: baseline;
    border-bottom: 1px solid var(--rule);
    padding: 0 4px 4px 2px;
    font: 18px "Marcellus", serif; color: var(--ink);
  }
  .dish__price { font-family: "Marcellus", serif; letter-spacing: 1px; }
  .dish__desc {
    margin-top: 5px; padding-left: 2px;
    font: 13px/17px "Mako", sans-serif; color: var(--ink-soft);
  }

  .section-title {
    position: absolute; height: 34px; padding: 0 14px 0 8px;
    background: var(--brush-red);
    border-radius: 3px 12px 4px 10px;
    font: 700 28px/34px "Alegreya", serif; color: #fff;
    white-space: nowrap;
  }

  .photo-strip {
    position: absolute; top: 755px; height: 102px;
    background:
      radial-gradient(circle at 12% 50%, #e9e3d6 0 46px, transparent 47px),
      radial-gradient(circle at 37% 50%, #e9e3d6 0 46px, transparent 47px),
      radial-gradient(circle at 62% 50%, #e9e3d6 0 46px, transparent 47px),
      radial-gradient(circle at 88% 50%, #e9e3d6 0 46px, transparent 47px),
      linear-gradient(90deg, var(--chili-dark), var(--chili-mid), var(--chili-dark), var(--chili-mid), var(--chili-dark));
  }
  .photo-strip--left { left: 22px; width: 570px; }
  .photo-strip--right { left: 609px; width: 570px; }
</style>
</head>
<body>
<main class="canvas">

  <section class="menu-page menu-page--left">
    <span class="page-number">page 3</span>

    <article class="dish" style="top:39px">
      <h3 class="dish__head"><span>Blanquillos con Jamón</span><span class="dish__price">00.00</span></h3>
      <p class="dish__desc">Tan Cociditos como a Usté le Gusten y con Blanquillos de Granja, de Rancho o Puras Claras (de Granja o de Rancho) acompañados de Frijolitos de la Casa.</p>
    </article>

    <article class="dish" style="top:122px">
      <h3 class="dish__head"><span>Blanquillos a la Mexicana</span><span class="dish__price">00.00</span></h3>
      <p class="dish__desc">Con jitomatito, cebollita y chilito verdi y pueden ser con Blanquillos de Granja, de Rancho o Puras Claras.</p>
    </article>

    <article class="dish" style="top:197px">
      <h3 class="dish__head"><span>Blanquillos con Nopales</span><span class="dish__price">00.00</span></h3>
      <p class="dish__desc">Tan Cociditos como a Usté le Gusten con Nopalitos Revolviditos con los Blanquillos y Frijolitos de la Casa.</p>
    </article>

    <article class="dish" style="top:279px">
      <h3 class="dish__head"><span>Blanquillos Rancheros</span><span class="dish__price">00.00</span></h3>
      <p class="dish__desc">Van Montados Sobre Dos Tortillitas de Maíz Blanco y Bañados de una Salsita Roja sin picante con Frijolitos de La Casa. Pueden ser con Blanquillos de Granja o de Rancho y tan cocidos como a Usté le gusten.</p>
    </article>

    <article class="dish" style="top:373px">
      <h3 class="dish__head"><span>Blanquillos con Salchicha</span><span class="dish__price">00.00</span></h3>
      <p class="dish__desc">ITan Cociditos como a Usté le Gusten Usamos pura Salchicha de Pavo y con Blanquillos de Granja, de Rancho o Puras Claras (También de Granja o de Rancho).</p>
    </article>

    <article class="dish" style="top:449px">
      <h3 class="dish__head"><span>Blanquillos con Tocino</span><span class="dish__price">00.00</span></h3>
      <p class="dish__desc">Tan Cociditos como a Usté le Gusten y el Tocino también lo puede Usté pedir Dorado, Medio Dorado o Fiestero (Medio Crudo) y con Blanquillos de Granja, de Rancho o Puras Claras.</p>
    </article>

    <h2 class="section-title" style="top:543px; left:6px">Los Tamales´n</h2>

    <article class="dish" style="top:587px">
      <h3 class="dish__head"><span>Empanada de Platano Macho</span><span class="dish__price">00.00</span></h3>
      <p class="dish__desc">Una de las Mejores Creaciones de Nuestra Cocina. La empanadita está hecha con masa de plátano Macho rellena de Pollito en Adobo sobre un espejo de Nuestro Mole Artesanal de 36 Ingredientes.</p>
    </article>
  </section>

  <div class="photo-strip photo-strip--left" role="img" aria-label="Fotografías de platillos sobre fondo de chiles secos: huevos rancheros, huevos revueltos con frijoles, empanada con mole y tamal en hoja"></div>

  <section class="menu-page menu-page--right">
    <span class="page-number">page 4</span>

    <article class="dish" style="top:38px">
      <h3 class="dish__head"><span>Tamal Oaxaqueño</span><span class="dish__price">00.00</span></h3>
      <p class="dish__desc">Sabroso Tamal relleno de Cerdo Adobadito envuelto en Hoja de Vástago con Frijolitos de La Casa.</p>
    </article>

    <article class="dish" style="top:114px">
      <h3 class="dish__head"><span>Tamal de Mole Colorao</span><span class="dish__price">00.00</span></h3>
      <p class="dish__desc">Dos Tamales envolvidos en Hoja de Maíz rellenos de Cerdito en Mole Colorao.</p>
    </article>

    <article class="dish" style="top:177px">
      <h3 class="dish__head"><span>Tamal de Mole Verdi</span><span class="dish__price">00.00</span></h3>
      <p class="dish__desc">Dos Tamales envolvidos en Hoja de Maíz rellenos de Cerdito en Mole Verdi.</p>
    </article>

    <h2 class="section-title" style="top:236px; left:14px">Los Sopes´n</h2>

    <article class="dish" style="top:284px">
      <h3 class="dish__head"><span>Sopes de Chicharrón de Carnitas</span><span class="dish__price">00.00</span></h3>
      <p class="dish__desc">¡ Haaa que Chicharrón... Y Haaa que Carnitas, Nuestra Receta Nuncamente Superada !</p>
    </article>

    <article class="dish" style="top:340px">
      <h3 class="dish__head"><span>Sopes de Papas con Chorizo</span><span class="dish__price">00.00</span></h3>
      <p class="dish__desc">Información del platillo</p>
    </article>

    <article class="dish" style="top:395px">
      <h3 class="dish__head"><span>Sopes Surtidos</span><span class="dish__price">00.00</span></h3>
      <p class="dish__desc">¡ POS LA VERDAD, SÍ SON BIEN SOPES ! Uno de Frijolitos, Uno de Papas Con Chorizo, Uno de Rajas y Otro más de Chicharrón de Carnitas.</p>
    </article>

    <article class="dish" style="top:468px">
      <h3 class="dish__head"><span>Sopes de Frijolitos´n</span><span class="dish__price">00.00</span></h3>
      <p class="dish__desc">Información del platillo</p>
    </article>

    <article class="dish" style="top:527px">
      <h3 class="dish__head"><span>Sopes con Rajas y Panela</span><span class="dish__price">00.00</span></h3>
      <p class="dish__desc">Sopecitos con Rajas y Nuestra Panela Artesanal elaborada por nosotros mismos en Nuestra Quesería.</p>
    </article>

    <h2 class="section-title" style="top:604px; left:22px">Las Gorditas</h2>

    <article class="dish" style="top:650px">
      <h3 class="dish__head"><span>Gorditas con Chicharrón de Carnitas</span><span class="dish__price">00.00</span></h3>
      <p class="dish__desc">! Nuestra Receta de Chicharrón de Carnitas es Única y Nuncamente Superada ¡</p>
    </article>
  </section>

  <div class="photo-strip photo-strip--right" role="img" aria-label="Fotografías de platillos sobre fondo de chiles secos: tamal con pimiento, sopes rojos, sopes verdes y gorditas"></div>

</main>
</body>
</html>
```